Postcard Design

Marlow Painting-all types of painting and staining-house,deck and roof powerwashing-stone and masonry sealing-
30 years in business-licensed and insured
Ray Marlow
Marlowtrio@quillnet.com
5076182243

Industry/Entity Type

Painting

```html
<!DOCTYPE html>
<html lang="en">
<head>
<meta charset="utf-8">
<title>Marlow Painting Postcard</title>
<link rel="stylesheet" href="https://fonts.googleapis.com/css2?family=Archivo+Black&family=Archivo+Narrow:wght@700&family=Arimo:wght@400;700&display=swap">
<style>
  :root {
    --purple: #5b4478;
    --purple-dark: #43305c;
    --purple-light: #7a6196;
    --ink: #1c1c1c;
    --grey-top: #f2f2f2;
    --grey-bottom: #cfcfcf;
    --white: #ffffff;
    --rule: #b9b9b9;
    --star-red: #d9334a;
    --star-green: #7bbf2a;
    --star-gold: #e0a526;
  }
  * { box-sizing: border-box; margin: 0; padding: 0; }
  html, body { width: 1200px; height: 1173px; overflow: hidden; background: var(--white); }
  body { position: relative; font-family: "Arimo", Arial, sans-serif; }

  .side-label { position: absolute; left: 238px; font-size: 22px; color: #444; }
  .side-label.front-label { top: 22px; }
  .side-label.back-label { top: 597px; }

  .card {
    position: absolute; left: 233px; width: 736px; height: 526px;
    border: 1.5px solid #333; overflow: hidden;
  }
  .card-front { top: 56px; background: linear-gradient(180deg, var(--grey-top), var(--grey-bottom)); }
  .card-back { top: 627px; background: var(--white); }

  .services { position: absolute; list-style: none; font-family: "Archivo Narrow", "Arial Narrow", sans-serif; font-weight: 700; color: var(--purple); text-transform: uppercase; }
  .services li { display: flex; align-items: center; gap: 9px; }
  .services .star { font-size: 0.8em; }
  .star.red { color: var(--star-red); }
  .star.green { color: var(--star-green); }
  .star.gold { color: var(--star-gold); }
  .card-front .services { left: 303px; top: 54px; font-size: 19px; line-height: 23px; }
  .card-back .services { left: 26px; top: 210px; font-size: 16px; line-height: 20px; }

  .brand-name {
    position: absolute; display: flex; align-items: center; gap: 14px;
    font-family: "Archivo Black", Arial, sans-serif; color: var(--purple); text-transform: uppercase; line-height: 1.02;
  }
  .brand-name .mark { background: var(--purple); flex: none; }
  .brand-name .name-line { display: block; }
  .card-front .brand-name { left: 316px; top: 178px; font-size: 50px; }
  .card-front .brand-name .mark { width: 30px; height: 30px; }
  .card-back .brand-name { left: 30px; top: 80px; font-size: 32px; }
  .card-back .brand-name .mark { width: 22px; height: 22px; }

  .anniversary { position: absolute; left: 30px; top: 268px; width: 270px; height: 110px; }
  .anniversary .big-number { position: absolute; left: 0; top: 0; font-family: "Arimo", Arial, sans-serif; font-size: 92px; line-height: 1; color: var(--ink); letter-spacing: -4px; }
  .anniversary .years { position: absolute; left: 110px; top: 18px; font-family: "Archivo Black", Arial, sans-serif; font-size: 17px; color: var(--ink); }
  .anniversary .ribbon {
    position: absolute; left: 40px; top: 70px; width: 222px; height: 24px;
    background: var(--ink); color: var(--white); transform: rotate(-5deg);
    font-family: "Archivo Narrow", sans-serif; font-weight: 700; font-size: 11px;
    display: flex; align-items: center; justify-content: center; text-transform: uppercase;
  }

  .colour-band {
    position: absolute; left: 0; top: 380px; width: 100%; height: 11px;
    background: linear-gradient(90deg, #e8a23a, #d9334a 25%, #8a3fa0 50%, #d13b8c 70%, #5b4478);
  }
  .contact-band {
    position: absolute; left: 0; top: 391px; width: 100%; height: 135px;
    background: linear-gradient(90deg, var(--purple-dark), var(--purple-light) 55%, var(--purple-dark));
  }
  .contact { position: absolute; left: 30px; top: 402px; color: var(--white); }
  .contact .person { font-family: "Archivo Black", Arial, sans-serif; font-size: 30px; letter-spacing: 1px; text-transform: uppercase; }
  .contact .email { font-family: "Arimo", Arial, sans-serif; font-weight: 700; font-size: 21px; margin-top: 2px; }
  .contact .phone { font-family: "Archivo Black", Arial, sans-serif; font-size: 36px; margin-top: 10px; letter-spacing: 1px; }

  .worker-figure {
    position: absolute; left: 560px; top: 80px; width: 176px; height: 446px;
    background: linear-gradient(180deg, rgba(255,255,255,0.85), rgba(255,255,255,0.55));
    clip-path: polygon(45% 0, 75% 0, 100% 30%, 100% 100%, 0 100%, 20% 60%, 40% 25%);
  }

  .card-back .phone {
    position: absolute; left: 26px; top: 285px;
    font-family: "Archivo Black", Arial, sans-serif; font-size: 32px; color: var(--purple);
  }
  .divider { position: absolute; left: 369px; top: 85px; width: 1px; height: 405px; background: var(--rule); }
  .stamp-box { position: absolute; left: 624px; top: 27px; width: 91px; height: 96px; border: 1.5px solid #888; }
  .address-line { position: absolute; left: 405px; width: 276px; height: 1px; background: var(--rule); }
  .address-line.line-1 { top: 322px; }
  .address-line.line-2 { top: 373px; }
  .address-line.line-3 { top: 424px; }
</style>
</head>
<body>
  <div class="side-label front-label">front</div>
  <section class="card card-front">
    <ul class="services">
      <li><span class="star red">★</span>All types of painting and staining-house</li>
      <li><span class="star green">★</span>Deck and roof powerwashing</li>
      <li><span class="star gold">★</span>Stone and masonry sealing</li>
    </ul>
    <div class="worker-figure" role="img" aria-label="Silhouette of a painter with a spray wand standing by a ladder"></div>
    <div class="brand-name"><span class="mark"></span><span class="name-text"><span class="name-line">Marlow</span><span class="name-line">Painting</span></span></div>
    <div class="anniversary">
      <span class="big-number">30</span>
      <span class="years">YEARS</span>
      <span class="ribbon">In business-licensed and insured</span>
    </div>
    <div class="colour-band"></div>
    <div class="contact-band"></div>
    <div class="contact">
      <div class="person">Ray Marlow</div>
      <div class="email">Marlowtrio@quillnet.com</div>
      <div class="phone">TEL. 5076182243</div>
    </div>
  </section>

  <div class="side-label back-label">back</div>
  <section class="card card-back">
    <div class="brand-name"><span class="mark"></span><span class="name-text"><span class="name-line">Marlow</span><span class="name-line">Painting</span></span></div>
    <ul class="services">
      <li><span class="star red">★</span>All types of painting and staining-house</li>
      <li><span class="star green">★</span>Deck and roof powerwashing</li>
      <li><span class="star gold">★</span>Stone and masonry sealing</li>
    </ul>
    <div class="phone">TEL. 5076182243</div>
    <div class="divider"></div>
    <div class="stamp-box"></div>
    <div class="address-line line-1"></div>
    <div class="address-line line-2"></div>
    <div class="address-line line-3"></div>
  </section>
</body>
</html>
```